VELMARA IMAGING
Ultrasound Imaging Services
VELMARA IMAGING - Imaging
Creative Brief
Professional
Dorvan Tessliff
Ultrasound Diagnostic
5873 Calloway ridge ln Raleigh, NC 27614
dorvantessliff@mailvane.net
Concepts
Logo for mobile ultrasound

```html
<!DOCTYPE html>
<html lang="en">
<head>
<meta charset="utf-8">
<title>Velmara Imaging – Business Card</title>
<link rel="stylesheet" href="https://fonts.googleapis.com/css2?family=Montserrat:wght@400;600;800&display=swap">
<style>
  :root {
    --navy: #1c1f6e;
    --sky: #3fa9dc;
    --sky-light: #8fd0ef;
    --ink: #1c1f6e;
    --grey: #5a5a66;
    --paper: #ffffff;
    --backdrop: #e6e8ec;
  }
  * { margin: 0; padding: 0; box-sizing: border-box; }
  html, body { width: 1200px; height: 901px; overflow: hidden; }
  body {
    background: var(--backdrop);
    font-family: "Montserrat", sans-serif;
    display: flex; align-items: center; justify-content: center;
  }
  .card {
    position: relative;
    width: 1000px; height: 571px;
    background: var(--paper);
    border-radius: 40px;
    overflow: hidden;
    box-shadow: 0 10px 30px rgba(0,0,0,0.12);
  }
  .card-art { position: absolute; inset: 0; width: 100%; height: 100%; }
  .brand {
    position: absolute; left: 80px; top: 170px;
    display: flex; flex-direction: column; align-items: flex-start;
  }
  .brand-row { display: flex; align-items: center; gap: 14px; }
  .brand-dot { width: 34px; height: 34px; border-radius: 50%; background: var(--sky); }
  .brand-name { font-weight: 800; font-size: 58px; color: var(--navy); letter-spacing: 1px; line-height: 1; }
  .brand-sub { margin-top: 8px; margin-left: 48px; font-weight: 800; font-size: 20px; color: var(--navy); letter-spacing: 0.5px; }
  .brand-tag { margin-top: 6px; margin-left: 150px; font-weight: 600; font-size: 12px; color: var(--sky); letter-spacing: 1.5px; }
  .person { position: absolute; left: 80px; top: 350px; }
  .person-name { font-weight: 600; font-size: 28px; color: var(--navy); letter-spacing: 1px; }
  .person-role { margin-top: 6px; font-size: 18px; color: var(--grey); }
  .contact {
    position: absolute; right: 50px; top: 70px;
    color: #fff; text-align: right; font-size: 16px;
  }
  .contact-address { line-height: 1.45; margin-bottom: 26px; font-size: 17px; }
  .contact-line { display: flex; justify-content: flex-end; align-items: center; gap: 12px; height: 38px; }
  .contact-line svg { width: 20px; height: 20px; fill: #fff; }
</style>
</head>
<body>
  <div class="card">
    <svg class="card-art" viewBox="0 0 1000 571" preserveAspectRatio="none" aria-hidden="true">
      <path d="M560,0 C480,200 470,430 270,571 L340,571 C540,430 560,200 640,0 Z" fill="var(--sky-light)"/>
      <path d="M600,0 C520,200 510,430 310,571 L370,571 C570,430 590,200 660,0 Z" fill="var(--sky)"/>
      <path d="M650,0 C580,200 560,430 360,571 L1000,571 L1000,0 Z" fill="var(--navy)"/>
      <path d="M760,0 C860,30 940,20 1000,0 L1000,14 C930,40 850,40 760,0 Z" fill="var(--sky)"/>
    </svg>

    <div class="brand">
      <div class="brand-row">
        <span class="brand-dot"></span>
        <span class="brand-name">VELMARA</span>
      </div>
      <div class="brand-sub">IMAGING ULTRASOUND SERVICES</div>
      <div class="brand-tag">ACCURATE FAST ORGANIZED</div>
    </div>

    <div class="person">
      <div class="person-name">DORVAN TESSLIFF</div>
      <div class="person-role">Managing Director</div>
    </div>

    <div class="contact">
      <p class="contact-address">5873 Calloway ridge ln<br>Raleigh, NC 27614</p>
      <div class="contact-line">919 555 0142
        <svg viewBox="0 0 24 24"><path d="M6.6 10.8a15 15 0 0 0 6.6 6.6l2.2-2.2a1 1 0 0 1 1-.25 11.4 11.4 0 0 0 3.6.57 1 1 0 0 1 1 1V20a1 1 0 0 1-1 1A17 17 0 0 1 3 4a1 1 0 0 1 1-1h3.5a1 1 0 0 1 1 1c0 1.25.2 2.45.57 3.57a1 1 0 0 1-.25 1z"/></svg>
      </div>
      <div class="contact-line">919 555 0187
        <svg viewBox="0 0 24 24"><path d="M7 2h10a2 2 0 0 1 2 2v16a2 2 0 0 1-2 2H7a2 2 0 0 1-2-2V4a2 2 0 0 1 2-2zm0 3v13h10V5zm5 14.2a1 1 0 1 0 0 .01z"/></svg>
      </div>
      <div class="contact-line">919 555 0193
        <svg viewBox="0 0 24 24"><path d="M6 3h12v5H6zM4 9h16a2 2 0 0 1 2 2v6h-4v4H6v-4H2v-6a2 2 0 0 1 2-2zm4 7v3h8v-3z"/></svg>
      </div>
      <div class="contact-line">dorvantessliff@mailvane.net
        <svg viewBox="0 0 24 24"><path d="M3 5h18v14H3zm2 2v.5l7 5 7-5V7zm0 3v7h14v-7l-7 5z"/></svg>
      </div>
      <div class="contact-line">www.velmaraimaging.net
        <svg viewBox="0 0 24 24"><path d="M12 2a10 10 0 1 0 0 20 10 10 0 0 0 0-20zm0 2c1 0 2.2 2 2.7 5H9.3C9.8 6 11 4 12 4zM4.3 11h3a16 16 0 0 0 0 2h-3a8 8 0 0 1 0-2zm5 0h5.4a14 14 0 0 1 0 2H9.3a14 14 0 0 1 0-2zm7.4 0h3a8 8 0 0 1 0 2h-3a16 16 0 0 0 0-2zM9.3 15h5.4c-.5 3-1.7 5-2.7 5s-2.2-2-2.7-5z"/></svg>
      </div>
    </div>
  </div>
</body>
</html>
```